WordPress Website for Pain Relief Clinic

I need a WordPress website designed for my laser pain relief clinic. It needs to be a professional, responsive design with 7 pages: Home, Why Choose Us, Treatable Conditions, Testimonials, FAQ, Franchising, Contact Us. Here is logo: https://s3.cloudvexa-store.net/media.b-r-t-n.net/sitebuilder/361/KelvaroLogoHighQuality.png

Target Market(s)

people with pain,elderly adults,injuries,soreness

Industry/Entity Type

Clinic

Number of Pages Required

5+ page

Colors
0792cd
85abd2

```html
<!DOCTYPE html>
<html lang="en">
<head>
<meta charset="utf-8">
<title>Kelvaro Laser Pain Relief</title>
<link rel="stylesheet" href="https://fonts.googleapis.com/css2?family=Open+Sans:wght@400;600;700;800&display=swap">
<style>
:root{
  --accent:#45bde2;
  --accent-dark:#0792cd;
  --soft-blue:#85abd2;
  --ink:#333b42;
  --muted:#8a9299;
  --line:#e3e6e9;
  --panel:#f1f2f4;
  --dark:#2d3135;
  --darker:#222528;
  --white:#ffffff;
}
*{margin:0;padding:0;box-sizing:border-box}
html,body{width:1200px;height:2664px;overflow:hidden;background:var(--white)}
body{font-family:"Open Sans",Arial,sans-serif;color:var(--ink);position:relative}
.container{width:880px;margin:0 auto;position:relative}
.btn{display:inline-block;font-weight:700;font-size:13px;letter-spacing:.5px;text-transform:uppercase;border-radius:3px;padding:11px 24px}
.btn-accent{background:var(--accent);color:var(--white)}
.btn-outline{border:2px solid var(--ink);color:var(--ink);background:transparent}
.btn-outline-light{border:2px solid var(--white);color:var(--white)}

/* top bar */
.topbar{height:32px;border-bottom:1px solid var(--line);font-size:11px;color:var(--muted)}
.topbar .container{display:flex;align-items:center;height:32px;gap:40px}
.topbar .account{margin-left:auto;display:flex;gap:18px}
.topbar span{display:flex;align-items:center;gap:6px}

/* header */
.site-header{height:76px}
.site-header .container{display:flex;align-items:center;height:76px}
.brand{font-size:17px;font-weight:700;color:var(--accent-dark);letter-spacing:.5px}
.main-nav{margin-left:auto;display:flex;height:76px}
.main-nav a{display:flex;align-items:center;padding:0 14px;font-size:11px;font-weight:600;color:var(--ink);text-transform:uppercase;border-left:1px solid var(--line);position:relative}
.main-nav a.active{color:var(--accent-dark)}
.main-nav a.active::after{content:"";position:absolute;left:0;right:0;bottom:0;height:3px;background:var(--accent)}

/* hero */
.hero{height:404px;position:relative;background:linear-gradient(100deg,#c9cdd1 0%,#e5e3e0 35%,#d4c6bc 60%,#a8968a 100%);text-align:center;color:var(--white)}
.hero::before{content:"";position:absolute;inset:0;background:rgba(30,35,40,.28)}
.hero-inner{position:relative;padding-top:92px}
.hero h1{font-size:38px;font-weight:800;letter-spacing:1px;text-shadow:0 2px 6px rgba(0,0,0,.35)}
.hero p{font-size:13px;font-weight:600;margin-top:14px;letter-spacing:.5px}
.hero .btn{margin-top:30px}
.hero-dots{position:absolute;bottom:18px;left:0;right:0;display:flex;justify-content:center;gap:8px}
.hero-dots i{width:9px;height:9px;border-radius:50%;background:rgba(255,255,255,.55)}
.hero-dots i.on{background:var(--white)}

/* features */
.features{height:292px;padding-top:86px}
.features .container{display:flex}
.feature{width:220px;text-align:center;padding:0 22px}
.feature svg{width:44px;height:44px}
.feature h3{font-size:14px;font-weight:700;margin-top:18px}
.feature p{font-size:11px;color:var(--muted);line-height:1.6;margin-top:10px}

/* team */
.team{background:var(--panel);height:928px;padding-top:152px;text-align:center}
.section-title{font-size:28px;font-weight:800;letter-spacing:1px;line-height:1.25;text-transform:uppercase}
.title-rule{width:60px;height:2px;background:var(--ink);margin:16px auto 0}
.team .intro{width:880px;margin:22px auto 0;font-size:11px;color:var(--muted);line-height:1.7}
.team .btn{margin-top:30px}
.team-cards{display:flex;justify-content:space-between;width:880px;margin:46px auto 0}
.card{width:260px;background:var(--white);text-align:left;height:480px}
.card-photo{height:268px;position:relative}
.photo-a{background:linear-gradient(160deg,#a7a39c,#e9e6e1 55%,#8d8174)}
.photo-b{background:linear-gradient(160deg,#d9e6ec,#b9cdd6)}
.photo-c{background:linear-gradient(160deg,#eef0f2,#c7cdd3 60%,#7b6656)}
.photo-b .overlay{position:absolute;inset:0;background:rgba(69,189,226,.55);display:flex;align-items:center;justify-content:center;gap:12px}
.photo-b .overlay i{width:30px;height:30px;border-radius:50%;border:2px solid var(--white)}
.card-body{padding:18px 20px}
.card h4{font-size:13px;font-weight:700}
.card .role{font-size:10px;color:var(--muted);margin-top:4px}
.card .bio{font-size:11px;color:var(--muted);line-height:1.6;margin-top:14px}
.card .more{display:block;text-align:center;font-size:11px;font-weight:700;margin-top:22px;border-top:1px solid var(--line);padding-top:16px}

/* difference */
.difference{height:492px;background:linear-gradient(120deg,#3a3f44,#2a2d31 60%,#34383d);color:var(--white);padding-top:92px;text-align:center}
.difference .title-rule{background:var(--white)}
.diff-grid{display:grid;grid-template-columns:repeat(3,300px);row-gap:38px;width:900px;margin:38px auto 0;text-align:left}
.diff-item{display:flex;gap:14px}
.diff-item svg{width:34px;height:34px;flex:none}
.diff-item h4{font-size:13px;font-weight:700;text-transform:uppercase;letter-spacing:.5px}
.diff-item p{font-size:11px;color:#b6bcc2;line-height:1.55;margin-top:4px;width:200px}
.difference .btn{margin-top:48px}

/* patients band */
.patients{height:112px;margin-top:28px;background:var(--accent);color:var(--white)}
.patients .container{display:flex;align-items:center;height:112px;justify-content:center;gap:48px}
.patients h5{font-size:14px;font-weight:700;text-transform:uppercase}
.btn-white{background:var(--white);color:var(--ink);padding:11px 44px}

/* footer */
.site-footer{background:var(--dark);height:268px;margin-top:20px;color:#b6bcc2}
.site-footer .container{display:flex;padding-top:38px}
.footer-col{width:320px;padding-right:40px}
.footer-col h6{font-size:13px;font-weight:700;color:var(--white);text-transform:uppercase;margin-bottom:18px}
.footer-col p{font-size:11px;line-height:1.6}
.footer-col .btn{margin-top:18px;font-size:11px;padding:9px 18px}
.post{margin-bottom:16px}
.post .date{font-size:10px;color:var(--muted);margin-top:2px}
.field{height:30px;background:#3c4146;border:1px solid #4a5056;font-size:11px;color:var(--muted);padding:7px 10px;margin-bottom:10px;width:240px}
.bottombar{position:absolute;left:0;right:0;bottom:0;height:44px;background:var(--darker);font-size:10px;color:var(--muted)}
.bottombar .container{display:flex;align-items:center;height:44px}
.bottombar nav{margin-left:auto;display:flex;gap:26px}
</style>
</head>
<body>

<div class="topbar">
  <div class="container">
    <span><svg width="12" height="9" viewBox="0 0 12 9"><rect x=".5" y=".5" width="11" height="8" fill="none" stroke="#8a9299"/><path d="M.5 .5 6 5l5.5-4.5" fill="none" stroke="#8a9299"/></svg>info@kelvaro-clinic.com</span>
    <span><svg width="10" height="10" viewBox="0 0 10 10"><path d="M2 1l2 2-1 1.5c.8 1.4 1.6 2.2 3 3L7.5 6.5l2 2L8 10C4 9.5.5 6 0 2z" fill="#8a9299"/></svg>(555) 014-2290</span>
    <div class="account"><span>Login</span><span>Sign up</span></div>
  </div>
</div>

<header class="site-header">
  <div class="container">
    <div class="brand">KELVARO LASER PAIN RELIEF</div>
    <nav class="main-nav">
      <a class="active">Home</a><a>Clinic</a><a>Our Staff</a><a>Resources</a><a>Contact Us</a>
    </nav>
  </div>
</header>

<section class="hero" role="img" aria-label="Photo of a clinician applying laser light therapy to a patient's leg">
  <div class="hero-inner">
    <h1>THE DOCTOR'S OFFICE, REINVENTED</h1>
    <p>A FRESH, CALMING APPROACH TO LASER PAIN CARE</p>
    <span class="btn btn-accent">About Doctors</span>
  </div>
  <div class="hero-dots"><i class="on"></i><i></i></div>
</section>

<section class="features">
  <div class="container">
    <div class="feature">
      <svg viewBox="0 0 44 44"><rect x="5" y="12" width="34" height="24" rx="3" fill="#45bde2"/><rect x="16" y="7" width="12" height="7" rx="2" fill="none" stroke="#45bde2" stroke-width="3"/><path d="M22 18v12M16 24h12" stroke="#fff" stroke-width="3"/></svg>
      <h3>Advanced Technology</h3>
      <p>Gentle laser care that targets the source of pain and speeds healing.</p>
    </div>
    <div class="feature">
      <svg viewBox="0 0 44 44"><circle cx="22" cy="22" r="17" fill="none" stroke="#45bde2" stroke-width="3"/><path d="M22 12v10l7 5" fill="none" stroke="#45bde2" stroke-width="3"/></svg>
      <h3>24/7 Availability</h3>
      <p>Our team answers your questions day or night, every day of the week.</p>
    </div>
    <div class="feature">
      <svg viewBox="0 0 44 44"><path d="M22 36 8 22a8 8 0 0 1 14-10 8 8 0 0 1 14 10z" fill="#45bde2"/><path d="M22 18v10M17 23h10" stroke="#fff" stroke-width="3"/></svg>
      <h3>Healthcare Solutions</h3>
      <p>Care plans built around your body, your goals and your daily life.</p>
    </div>
    <div class="feature">
      <svg viewBox="0 0 44 44"><circle cx="22" cy="12" r="7" fill="#45bde2"/><path d="M8 38c0-9 6-15 14-15s14 6 14 15z" fill="#45bde2"/></svg>
      <h3>Patient and Visitor Guide</h3>
      <p>Everything you need to know before your first visit with us.</p>
    </div>
  </div>
</section>

<section class="team">
  <h2 class="section-title">Meet Our<br>Clinic Care Team</h2>
  <div class="title-rule"></div>
  <p class="intro">Our caring specialists bring years of training in laser therapy and pain relief. Each visit starts with listening, so we understand your pain and build a plan that fits you. From sore joints to sports injuries, we help patients of every age move more freely and live with greater comfort each day.</p>
  <span class="btn btn-outline">Meet the Full Team</span>
  <div class="team-cards">
    <div class="card">
      <div class="card-photo photo-a" role="img" aria-label="Portrait photo of a doctor with a stethoscope"></div>
      <div class="card-body">
        <h4>Dr. Aldren Voss</h4>
        <div class="role">Senior Pain Specialist</div>
        <p class="bio">Focused on joint pain and gentle recovery for older adults.</p>
        <span class="more">SEE FULL PROFILE</span>
      </div>
    </div>
    <div class="card">
      <div class="card-photo photo-b" role="img" aria-label="Portrait photo of a doctor in a white coat">
        <div class="overlay"><i></i><i></i><i></i></div>
      </div>
      <div class="card-body">
        <h4>Dr. Mattis Orlen</h4>
        <div class="role">Laser Therapy Lead</div>
        <p class="bio">Guides patients through safe, modern laser treatment plans.</p>
        <span class="more">SEE FULL PROFILE</span>
      </div>
    </div>
    <div class="card">
      <div class="card-photo photo-c" role="img" aria-label="Portrait photo of a smiling doctor"></div>
      <div class="card-body">
        <h4>Dr. Sela Brink</h4>
        <div class="role">Sports Injury Doctor</div>
        <p class="bio">Helps active patients heal soreness and return to motion.</p>
        <span class="more">SEE FULL PROFILE</span>
      </div>
    </div>
  </div>
</section>

<section class="difference">
  <h2 class="section-title">What Makes Us Different?</h2>
  <div class="title-rule"></div>
  <div class="diff-grid">
    <div class="diff-item">
      <svg viewBox="0 0 34 34"><path d="M9 4h16v9a8 8 0 0 1-16 0z" fill="#45bde2"/><path d="M9 7H4c0 5 2 8 5 8M25 7h5c0 5-2 8-5 8" fill="none" stroke="#45bde2" stroke-width="2"/><rect x="15" y="20" width="4" height="7" fill="#45bde2"/><rect x="10" y="27" width="14" height="3" fill="#45bde2"/></svg>
      <div><h4>Award Winning Care</h4><p>Trusted treatment praised by local patients.</p></div>
    </div>
    <div class="diff-item">
      <svg viewBox="0 0 34 34"><circle cx="13" cy="10" r="6" fill="#45bde2"/><path d="M2 30c0-8 5-12 11-12s11 4 11 12z" fill="#45bde2"/><path d="M28 10v10M23 15h10" stroke="#45bde2" stroke-width="3"/></svg>
      <div><h4>Total Provider Access</h4><p>Reach your care team whenever you need.</p></div>
    </div>
    <div class="diff-item">
      <svg viewBox="0 0 34 34"><circle cx="17" cy="13" r="9" fill="#45bde2"/><rect x="12" y="22" width="10" height="4" fill="#45bde2"/><rect x="13" y="28" width="8" height="3" fill="#45bde2"/></svg>
      <div><h4>Latest Technology</h4><p>Modern lasers for fast and gentle relief.</p></div>
    </div>
    <div class="diff-item">
      <svg viewBox="0 0 34 34"><circle cx="17" cy="17" r="14" fill="none" stroke="#45bde2" stroke-width="3"/><path d="M7 7l20 20" stroke="#45bde2" stroke-width="3"/></svg>
      <div><h4>No More Paperwork</h4><p>Simple online forms before your first visit.</p></div>
    </div>
    <div class="diff-item">
      <svg viewBox="0 0 34 34"><rect x="3" y="6" width="28" height="25" rx="2" fill="none" stroke="#45bde2" stroke-width="3"/><path d="M3 13h28M10 3v6M24 3v6" stroke="#45bde2" stroke-width="3"/><path d="M11 21l4 4 8-8" fill="none" stroke="#45bde2" stroke-width="3"/></svg>
      <div><h4>No Hassle Appointments</h4><p>Book a time that suits your busy week.</p></div>
    </div>
    <div class="diff-item">
      <svg viewBox="0 0 34 34"><path d="M17 32S6 20 6 13a11 11 0 0 1 22 0c0 7-11 19-11 19z" fill="#45bde2"/><circle cx="17" cy="13" r="4" fill="#2d3135"/></svg>
      <div><h4>Convenient Location</h4><p>Easy parking and step free clinic access.</p></div>
    </div>
  </div>
  <span class="btn btn-outline-light">Make a Appointment &nbsp;&rsaquo;</span>
</section>

<section class="patients">
  <div class="container">
    <h5>Accepting/Not Accepting New Patients</h5>
    <span class="btn btn-white">Check Here</span>
  </div>
</section>

<footer class="site-footer">
  <div class="container">
    <div class="footer-col">
      <h6>About Corlan Clinics</h6>
      <p>A friendly laser pain relief clinic helping people move with ease, heal faster and enjoy life again.</p>
      <span class="btn btn-accent">Physician Toolbox</span>
    </div>
    <div class="footer-col">
      <h6>Recent Post</h6>
      <div class="post"><p>How laser therapy eases stiff knees and aching backs.</p><div class="date">March 12, 2015</div></div>
      <div class="post"><p>Five easy stretches for a softer morning routine.</p><div class="date">March 04, 2015</div></div>
    </div>
    <div class="footer-col">
      <h6>Newsletter</h6>
      <div class="field">Your name</div>
      <div class="field">Your email</div>
      <span class="btn btn-accent">Subscribe Now</span>
    </div>
  </div>
  <div class="bottombar">
    <div class="container">
      <span>&copy; 2015 WEBSITE NAME</span>
      <nav><span>Contact Us</span><span>Terms &amp; Conditions</span><span>Policy</span></nav>
    </div>
  </div>
</footer>

</body>
</html>
```